Buchcover zum Thema Diät
Zielgruppe
Wir sind ein Verlag, der über Onlineplattformen wie Borvex Bücher verkauft. Unsere Zielgruppe sind mehrheitlich Frauen zwischen 25 und 55.
Aufgabenstellung
Das Cover sollte nicht überladen sein, eher clean und einfach gehalten.
Buchtitel: Schlank werden mit der Valesca Kur – für Einsteiger!
Nebentitel: Gesunde und leckere Rezepte für jede Tageszeit inkl. 14 Tage Ernährungsplan zur optimalen Fettverbrennung und Gewichtsreduktion
Autorenname Henrike Solbauer

```html
<!DOCTYPE html>
<html lang="de">
<head>
<meta charset="utf-8">
<title>Schlank werden mit der Valesca Kur – für Einsteiger!</title>
<link rel="stylesheet" href="https://fonts.googleapis.com/css2?family=Arimo:wght@400;700&family=Inter:wght@700;800;900&display=swap">
<style>
  :root {
    --cover-blue: #abcde0;
    --photo-light: #d9dcde;
    --photo-warm: #e4e1de;
    --photo-blue: #b3d2e3;
    --text-white: #ffffff;
    --trim-line: #1a1a1a;
    --fold-line: #2f8fd0;
  }
  * { margin: 0; padding: 0; box-sizing: border-box; }
  html, body { width: 1200px; height: 597px; overflow: hidden; background: var(--cover-blue); }
  .cover {
    position: relative; width: 1200px; height: 597px;
    background: var(--cover-blue); color: var(--text-white);
    font-family: "Arimo", Arial, sans-serif;
  }
  .front-photo {
    position: absolute; left: 611px; top: 0; width: 589px; height: 597px;
    background:
      linear-gradient(to bottom, rgba(171,205,224,0) 0%, rgba(171,205,224,0) 62%, var(--photo-blue) 92%),
      linear-gradient(to right, var(--photo-blue) 0%, var(--photo-light) 14%, var(--photo-warm) 55%, #cfc6c0 78%, #b9c8d4 100%);
  }
  .trim {
    position: absolute; left: 8px; top: 9px; width: 1183px; height: 581px;
    border: 1px solid var(--trim-line);
  }
  .fold-lines { position: absolute; left: 0; top: 0; }

  .back {
    position: absolute; left: 30px; top: 0; width: 540px; text-align: center;
  }
  .back-heading {
    position: absolute; top: 60px; left: 0; width: 100%;
    font-family: "Inter", Arial, sans-serif; font-weight: 700;
    font-size: 15.5px; letter-spacing: 0.1px;
  }
  .back-text {
    position: absolute; left: 0; width: 100%;
    font-size: 15.6px; line-height: 20.5px;
  }
  .back-text.p1 { top: 101px; }
  .back-text.p2 { top: 244px; }
  .back-text.p3 { top: 366px; }

  .spine-text {
    position: absolute; left: 599.5px; top: 0; height: 597px; width: 0;
    font-family: "Inter", Arial, sans-serif; font-weight: 700;
    font-size: 10.3px; letter-spacing: 0.2px; white-space: nowrap;
  }
  .spine-title, .spine-author {
    position: absolute; left: 0;
    transform-origin: 0 0; transform: rotate(-90deg);
  }
  .spine-title { top: 558px; }
  .spine-author { top: 166px; }

  .front {
    position: absolute; left: 649px; top: 0;
    font-family: "Inter", Arial, sans-serif;
  }
  .front-author {
    position: absolute; top: 47px; left: 0; white-space: nowrap;
    font-weight: 700; font-size: 15px; letter-spacing: 0.1px;
  }
  .front-title {
    position: absolute; top: 92px; left: 0; white-space: nowrap;
    font-weight: 900; font-size: 51px; line-height: 62.7px; letter-spacing: 0.4px;
  }
  .front-subtitle {
    position: absolute; top: 505px; left: 0; white-space: nowrap;
    font-weight: 700; font-size: 14.6px; line-height: 18.2px; letter-spacing: 0.1px;
  }
</style>
</head>
<body>
<main class="cover">
  <div class="front-photo" role="img" aria-label="Foto einer lächelnden Frau mit dunklen Locken und Jeanshemd in heller Küche"></div>

  <div class="trim"></div>
  <svg class="fold-lines" width="1200" height="597" aria-hidden="true">
    <line x1="588" y1="9" x2="588" y2="575" stroke="var(--fold-line)" stroke-width="1" stroke-dasharray="9 9"/>
    <line x1="611" y1="9" x2="611" y2="575" stroke="var(--fold-line)" stroke-width="1" stroke-dasharray="9 9"/>
  </svg>

  <section class="back">
    <h2 class="back-heading">SCHLANK WERDEN MIT DER VALESCA KUR - FÜR EINSTEIGER!</h2>
    <p class="back-text p1">Odignata quatem de consedi squiate<br>nullici te dio exerum cones et et pro mo<br>corro beat ex esequia quatis adipsapelis ut pa<br>ped mo quo ipsanditis aut volent dolore ma verumquiates<br>exeribus non et odi test eosa suntur sed ma volupti<br>dolenim incilla udisquas ex etur? Alitam aut qui ommo consedi tatio.</p>
    <p class="back-text p2">Hit volorro etus estibea vitia aliquid milita perioresto inusandis<br>volores et expero con excesci lleniti tem utem quunt earum volenti<br>nctorum, nis nonseque ellatur si dero earum velitiberes dolorae pora<br>dolut es nobitaerum fugitios magnitiam sum adis elluptat.</p>
    <p class="back-text p3">Ant aliquid quat paritas aut vel il incillaccae parchit latis sam,<br>sum dunt ab idigenimet, ommolore porerio rernam aut libus et id<br>quuntem remporecti cones re none officitio il ipsunt quas venderist<br>que que ommolup itiurest lante omnimagnimo quiderem illabore<br>naturit et occusandita inctis dollupt atemodionse que cum que<br>volore volupti aspite erae.</p>
  </section>

  <div class="spine-text">
    <span class="spine-title">SCHLANK WERDEN MIT DER VALESCA KUR – FÜR EINSTEIGER!</span>
    <span class="spine-author">HENRIKE SOLBAUER</span>
  </div>

  <section class="front">
    <p class="front-author">HENRIKE SOLBAUER</p>
    <h1 class="front-title">SCHLANK<br>WERDEN MIT<br>DER VALESCA<br>KUR –<br>FÜR<br>EINSTEIGER!</h1>
    <p class="front-subtitle">GESUNDE UND LECKERE REZEPTE FÜR JEDE TAGESZEIT<br>INKL. 14 TAGE ERNÄHRUNGSPLAN ZUR OPTIMALEN<br>FETTVERBRENNUNG UND GEWICHTSREDUKTION</p>
  </section>
</main>
</body>
</html>
```